Global Expert Network Firm needs business card design

We need business card design for a new company based in Seoul, South Korea called 'Corwell Insight Partners'. We recruit industry experts covering all countries and connect our client and recruited expert by phone, face-to-face meetings and etc. We are a global expert network firm that is focused on delivering high-quality experts to our clients throughout the world. Our clients include multinational corporations, global consulting firms, private equity firms, venture capital firms, asset management companies.
We have made new logo and please find attachment.(Please use new logo)
Target Market(s)
Global Consulting Firms, Investment Firms, Private Equity Firms, Venture Capital Firms.
Industry/Entity Type
Recruitment
Contact Information for Business Card
We need two Languages (English and Korean Version).
The front is Korean and the back is English version.
[The back] [English]
Company Name: Corwell Insight Partners, Inc.
CEO Name: Daniel Park
Address: #507, Hanbit Bldg, 82 Maebongsan-ro, Dobong-gu, Seoul, 01327, Korea
Tel. +82 2 718 4052
Fax. +82 2 864 1097
Mobile. +82 10 7264 8815
Email: daniel@corwellip.com
Web: www.corwellip.com
[The front] [Korean] => Described in same order as English version.
회사명: 코웰인사이트파트너스(주)
대표이사: 박도현
주소: 서울시 도봉구 매봉산로 82 한빛빌딩 507호
Tel. 02 718 4052
Fax. 02 864 1097
Mobile. 010 7264 8815
Web: www.corwellip.com
Look and feel
Each slider illustrates characteristics of the customer's brand and the style your logo design should communicate.

```html
<!DOCTYPE html>
<html lang="en">
<head>
<meta charset="utf-8">
<title>Corwell Insight Partners – Business Cards</title>
<link href="https://fonts.googleapis.com/css2?family=Cinzel:wght@600&family=Open+Sans:wght@400&family=Noto+Sans+KR:wght@400&display=swap" rel="stylesheet">
<style>
  :root{
    --backdrop:#8a5a34;
    --kraft-light:#d6b083;
    --kraft-mid:#c49a69;
    --kraft-dark:#b3844f;
    --ink:#1c140d;
    --rule:rgba(40,26,14,.55);
  }
  *{margin:0;padding:0;box-sizing:border-box}
  html,body{width:1200px;height:900px;overflow:hidden}
  body{background:var(--backdrop);position:relative;font-family:"Open Sans",sans-serif;color:var(--ink)}
  .card{
    position:absolute;left:330px;width:557px;height:343px;
    background:radial-gradient(ellipse at 30% 20%,var(--kraft-light),var(--kraft-mid) 55%,var(--kraft-dark));
    box-shadow:2px 4px 6px rgba(0,0,0,.45);
  }
  .card--english{top:90px}
  .card--korean{top:469px}
  .company-name{
    position:absolute;width:215px;
    font-family:"Open Sans",sans-serif;font-weight:400;
    font-size:30px;line-height:40px;color:var(--ink);
  }
  .card--english .company-name{left:38px;top:130px}
  .card--korean .company-name{left:53px;top:130px}
  .divider{position:absolute;top:45px;width:1px;height:240px;background:var(--rule)}
  .card--english .divider{left:277px}
  .card--korean .divider{left:291px}
  .details{position:absolute;font-size:15.5px;line-height:20px}
  .card--english .details{left:306px;top:44px}
  .card--korean .details{left:318px;top:56px;font-family:"Noto Sans KR","Open Sans",sans-serif;font-size:15px}
  .person-name{font-family:"Cinzel",serif;font-weight:600;font-size:20px;letter-spacing:.5px;line-height:24px}
  .contact-list{list-style:none}
  .contact-list li{display:flex;align-items:center;gap:4px}
  .contact-list svg{width:12px;height:12px;flex:none;fill:var(--ink)}
  .gap-s{height:6px}
  .gap-m{height:20px}
  .gap-k{height:10px}
  .address{font-style:normal}
  .card--korean .contact-list{font-family:"Open Sans",sans-serif;font-size:15.5px}
</style>
</head>
<body>
<svg width="0" height="0" style="position:absolute" aria-hidden="true">
  <defs>
    <symbol id="icon-phone" viewBox="0 0 12 12"><path d="M1 5c0-2 2-3 5-3s5 1 5 3H8.5V4h-5v1z M2.5 6.5h7l1 4h-9z"/></symbol>
    <symbol id="icon-fax" viewBox="0 0 12 12"><path d="M3 1h6v3H3z M1 5h10v4H9v2H3V9H1z M4 8v2h4V8z"/></symbol>
    <symbol id="icon-mobile" viewBox="0 0 12 12"><path d="M3 0.5h6v11H3z M4 2v7h4V2z"/></symbol>
    <symbol id="icon-mail" viewBox="0 0 12 12"><path d="M1 3h10v7H1z M1.5 3.5 6 7l4.5-3.5v-.2h-9z" fill-rule="evenodd"/></symbol>
    <symbol id="icon-web" viewBox="0 0 12 12"><circle cx="6" cy="6" r="5.2"/></symbol>
  </defs>
</svg>

<section class="card card--english">
  <div class="company-name">Corwell Insight Partners</div>
  <div class="divider"></div>
  <div class="details">
    <div class="person-name">DANIEL PARK</div>
    <div>CEO</div>
    <div class="gap-s"></div>
    <ul class="contact-list">
      <li><svg><use href="#icon-phone"/></svg>+82 2 718 4052</li>
      <li><svg><use href="#icon-fax"/></svg>+82 2 864 1097</li>
      <li><svg><use href="#icon-mobile"/></svg>+82 10 7264 8815</li>
      <li><svg><use href="#icon-mail"/></svg>daniel@corwellip.com</li>
      <li><svg><use href="#icon-web"/></svg>www.corwellip.com</li>
    </ul>
    <div class="gap-s"></div>
    <address class="address">
      Corwell Insight Partners, Inc.<br>
      #507, Hanbit Bldg, 82<br>
      Maebongsan-ro<br>
      Dobong-gu, Seoul<br>
      01327, Korea
    </address>
  </div>
</section>

<section class="card card--korean">
  <div class="company-name">Corwell Insight Partners</div>
  <div class="divider"></div>
  <div class="details">
    <div>박도현</div>
    <div>대표</div>
    <div class="gap-m"></div>
    <div>코웰인사이트파트너스(주)</div>
    <address class="address">
      서울시 도봉구 매봉산로 82<br>
      한빛빌딩 507호
    </address>
    <div class="gap-k"></div>
    <ul class="contact-list">
      <li><svg><use href="#icon-phone"/></svg>+82 2 718 4052</li>
      <li><svg><use href="#icon-fax"/></svg>+82 2 864 1097</li>
      <li><svg><use href="#icon-mobile"/></svg>+82 10 7264 8815</li>
      <li><svg><use href="#icon-mail"/></svg>daniel@corwellip.com</li>
      <li><svg><use href="#icon-web"/></svg>www.corwellip.com</li>
    </ul>
  </div>
</section>
</body>
</html>
```